Creative Magazine Ad - fusing comfort, culture and cuisine for a food supply company

Hello and welcome to this project!

We need an ad for our company, Larder Vale PNG, that is going to be in a magazine read by the Australian Army based in Papua New Guinea.

We want an ad that makes people stop and look. The key message is that even though Papua New Guinea is exotic, the food can be the same (as in Australia). And we want to show off what our company does – supplying great food that caters for all.

Your design should include:

Size:
• 1 page at 15cm height x 19.6cm width
Pictures:
• Our logo – Larder Vale PNG – where people can see it
• Pictures or elements that capture the tropical landscape, tribal culture and or essence of Papua New Guinea mixed with pictures of Australian food like barbeque, steaks, pies, roast vegetables etc.
Text to add:
• Title: "Taste of Home in the Tropics: Your Australian Culinary Guide in Papua New Guinea”
• Message: "Our mission is to manufacture and procure a diverse range of high-quality food products, catering to the unique needs of defence camps, and supplying small to large wholesalers, retailers, restaurants, hotels, and caterers throughout Papua New Guinea. We are dedicated to supporting our defence forces with the comforts of home, while serving the broader community with exceptional culinary offerings."
• And our contact details:
+675 341 6092
www.lvx.com.pg
sales@lardervalepng.com.pg

What we need:
• A graphic for printing for the magazine.
• A digital version to use online.

Thanks again – any questions please ask :)

A Bit About Us
Larder Vale PNG Ltd is a 100% PNG-owned and managed business and is proud to be one of the largest food supply companies in the country. Our ability to supply a wide range of premium imported, local and in-house manufactured products from our Butchery and Bakery has contributed to the rock-solid reputation for quality and services that Larder Vale now enjoys throughout PNG.

We are proud to also sell our wide range of products through our retail outlets (Gudi Grill Stoa, Gudi Crust Stoa and Tiki Grill Stoa) and our popular Quick Service Restaurants (Heron Wrapper and Kelo Tart Jar). Our Catering division (Gudi Rofa Catering) owns a vast array of commercial catering equipment and has experience catering for large-scale events in PNG. We are the only company in Papua New Guinea that has the technology to provide “tamper proof” cold and hot individual meal solutions that can be delivered in temperature-controlled vehicles to locations in Port Moresby but also as a solution to large-scale mining camp catering needs.

```html
<!DOCTYPE html>
<html lang="en">
<head>
<meta charset="utf-8">
<title>Larder Vale PNG — Taste of Home in the Tropics</title>
<link rel="stylesheet" href="https://fonts.googleapis.com/css2?family=Oswald:wght@500;700&family=Poppins:wght@400;600&family=Roboto+Condensed:ital,wght@1,600&display=swap">
<style>
  :root {
    --backdrop: #333333;
    --brand-red: #e31e24;
    --ink: #1d1d1d;
    --paper: #ffffff;
    --paper-grey: #efefef;
    --hill-dark: #3f4a35;
    --hill-mid: #6d7a57;
    --sky: #c9cfd3;
  }
  * { margin: 0; padding: 0; box-sizing: border-box; }
  html, body {
    width: 1200px; height: 1200px; overflow: hidden;
    background: var(--backdrop);
  }
  .ad {
    position: absolute; left: 52px; top: 176px;
    width: 1096px; height: 848px; overflow: hidden;
    background: var(--paper);
  }
  .ad-art { position: absolute; inset: 0; }
  .brand {
    position: absolute; left: 40px; top: 66px;
    display: flex; align-items: center; gap: 12px;
  }
  .brand-mark {
    width: 30px; height: 30px; border-radius: 50%;
    background: var(--brand-red);
  }
  .brand-name {
    font-family: "Oswald", sans-serif; font-weight: 700;
    font-size: 44px; line-height: 1; color: var(--paper);
  }
  .cert-badge {
    position: absolute; left: 192px; top: 38px;
    width: 62px; height: 22px; border-radius: 3px;
    background: var(--paper);
  }
  .tagline {
    position: absolute; left: 0; width: 286px; top: 170px;
    text-align: center;
    font-family: "Roboto Condensed", sans-serif; font-style: italic; font-weight: 600;
    font-size: 14px; color: var(--paper);
  }
  .headline {
    position: absolute; left: 0; width: 100%; top: 240px;
    text-align: center; color: var(--paper);
    font-family: "Oswald", sans-serif; font-weight: 700;
    text-shadow: 3px 3px 0 rgba(0,0,0,0.75);
  }
  .headline-main { display: block; font-size: 84px; line-height: 1.1; letter-spacing: 0.5px; }
  .headline-sub { display: block; font-size: 40px; line-height: 1.3; font-weight: 500; margin-top: 12px; }
  .food-photo {
    position: absolute; left: 26px; top: 485px;
    width: 410px; height: 280px; border-radius: 10px;
    border: 6px solid #d9d9d9;
    background: linear-gradient(135deg, #8a3a1e 0%, #b5562c 35%, #e8d27a 55%, #7a2418 80%, #5a2a1a 100%);
  }
  .mission {
    position: absolute; left: 455px; top: 597px; width: 608px;
    font-family: "Poppins", sans-serif; font-size: 17px; line-height: 25px;
    color: var(--ink); text-align: justify; text-align-last: right;
  }
  .contacts {
    position: absolute; left: 0; top: 786px; width: 100%;
    font-family: "Poppins", sans-serif; font-weight: 600; color: var(--brand-red);
  }
  .contact {
    position: absolute; display: flex; align-items: center; gap: 8px;
    font-size: 19px; white-space: nowrap;
  }
  .contact-icon {
    width: 28px; height: 28px; border-radius: 50%;
    background: var(--ink); display: flex; align-items: center; justify-content: center;
  }
  .contact-phone { left: 267px; }
  .contact-web { left: 501px; }
  .contact-mail { left: 742px; }
</style>
</head>
<body>
<main class="ad">
  <svg class="ad-art" viewBox="0 0 1096 848" width="1096" height="848" aria-hidden="false">
    <defs>
      <linearGradient id="landscape" x1="0" y1="0" x2="0" y2="1">
        <stop offset="0" stop-color="#c9cfd3"/>
        <stop offset="0.22" stop-color="#9aa39a"/>
        <stop offset="0.45" stop-color="#5d6a48"/>
        <stop offset="0.75" stop-color="#3d4731"/>
        <stop offset="1" stop-color="#6f7450"/>
      </linearGradient>
      <linearGradient id="lower-paper" x1="0" y1="0" x2="0" y2="1">
        <stop offset="0" stop-color="#ffffff"/>
        <stop offset="1" stop-color="#ececec"/>
      </linearGradient>
    </defs>
    <rect width="1096" height="848" fill="url(#lower-paper)"/>
    <path role="img" aria-label="Photo of forested mountain ranges in the Papua New Guinea highlands under a hazy sky"
          d="M0 0 H1096 V372 C980 450 820 500 632 482 C420 460 220 420 0 440 Z" fill="url(#landscape)"/>
    <path class="wave-red" d="M0 440 C220 420 420 460 632 482 C820 500 980 450 1096 372 V504 C1000 560 900 575 800 565 C560 545 300 470 0 452 Z" fill="var(--brand-red)"/>
    <path class="wave-grey" d="M1096 520 C1000 580 880 600 760 588 C700 582 640 570 560 552 L1096 560 Z" fill="#f4f4f4" opacity="0"/>
    <path class="splash-red" d="M0 600 L40 560 L60 640 L30 760 L120 780 L210 770 L240 800 L190 830 L120 848 L0 848 Z" fill="var(--brand-red)"/>
  </svg>

  <div class="cert-badge" aria-hidden="true"></div>
  <div class="brand">
    <span class="brand-mark"></span>
    <span class="brand-name">Larder Vale</span>
  </div>
  <p class="tagline">“100% PNG Owned &amp; Operated”</p>

  <h1 class="headline">
    <span class="headline-main">Taste of Home in the Tropics:</span>
    <span class="headline-sub">Your Australian Culinary Guide<br>in Papua New Guinea</span>
  </h1>

  <div class="food-photo" role="img" aria-label="Tray of barbecue: roast chicken, sliced brisket, sausages, pork ribs, pickles, jalapeños and onion"></div>

  <p class="mission">Our mission is to manufacture and procure a diverse range of high-quality food products, catering to the unique needs of defence camps, and supplying small to large wholesalers, retailers, restaurants, hotels, and caterers throughout Papua New Guinea. We are dedicated to supporting our defence forces with the comforts of home, while serving the broader community with exceptional culinary offerings.</p>

  <div class="contacts">
    <div class="contact contact-phone">
      <span class="contact-icon"><svg width="16" height="16" viewBox="0 0 24 24"><path d="M6.6 10.8a15 15 0 0 0 6.6 6.6l2.2-2.2c.3-.3.7-.4 1-.2 1.1.4 2.3.6 3.6.6.6 0 1 .4 1 1V20c0 .6-.4 1-1 1A17 17 0 0 1 3 4c0-.6.4-1 1-1h3.5c.6 0 1 .4 1 1 0 1.3.2 2.5.6 3.6.1.3 0 .7-.2 1z" fill="#fff"/></svg></span>
      +675 341 6092
    </div>
    <div class="contact contact-web">
      <span class="contact-icon"><svg width="18" height="18" viewBox="0 0 24 24" fill="none" stroke="#fff" stroke-width="1.6"><circle cx="12" cy="12" r="9"/><ellipse cx="12" cy="12" rx="4" ry="9"/><path d="M3 12h18M4.5 7.5h15M4.5 16.5h15"/></svg></span>
      www.lvx.com.pg
    </div>
    <div class="contact contact-mail">
      <span class="contact-icon"><svg width="16" height="16" viewBox="0 0 24 24" fill="none" stroke="#fff" stroke-width="1.8"><rect x="3" y="5" width="18" height="14" rx="1"/><path d="M3 6l9 7 9-7M3 18l7-6M21 18l-7-6"/></svg></span>
      sales@lardervalepng.com.pg
    </div>
  </div>
</main>
</body>
</html>
```